Guaranteed Job - Sleek Sexy Business Card UV Spot

Im looking for a sleek and sexy business card, that resembles elite or VIP status status.
our business is corinvale.example
you can view our products on there, but our main audience for handing out our cards will be for people in the hospitality industry, so it will need to impress high management and CEO of hotels and restaurants, bars, clubs etc...
the card features will have UV spot on both sides, 400gsm stock. standard size.
Artwork should be 86 x 54mm + 2mm bleed = 90 x 58mm
it should have a nice "unique" uv spot pattern that highlights the card, not a repeated pattern, theres no originality there, and it will be disregarded.
The written material will be:
Corin Vale Hospitality College (logo)
Tobin Marsh
Director
Phone: 1300 615 737
Mobile: 0455 817 296
Email: info@corinvale.example
website: www.corinvale.example
I'm looking for originality here, i don't want just a simple stock card, want something that has a wow factor for people.
You will find the logo attached. you may invert the white to black words to suit the background as you please.
thank you and good luck
As a side note, ive received a lot of proposals, im too busy to give feedback to each and every one, so if i havent provided feedback for your design within 24 hours, then consider it not acceptable, and you could resubmit another design.
So far i have not seen any design that stood out for me, they all seem pretty generic. there nothing thats unique, i would figure for the amount that im offering, that people would put some more effort and creativity into the design.
so far over 200 designs submitted, and nothing i have seen looks very original, everything looks like a different variation of the same stuff, i said it very clearly i wanted something unique, the only thing that has come close to it so far is this one
Reason: Ive received alot of design concepts and i have reviewed everyone, but i havent had time to give feedback to every single one, only the ones that have interested me, if i havent responded, its because i havent found it good enough.
so far only a few design have been on par with what ive been looking for, an attractive eye popping design.
heres a few of them,
http://files.pixelbazaar.example/design_img/51736/62418/62418_2840915_51736_image.jpg
http://files.pixelbazaar.example/design_img/51736/68254/68254_2841377_51736_image.jpg
theyre, both unique and original, and eye catching, the only thing theyre missing is the sexyness.
if you still think you have some creativity left in your minds, then throw it on here.
Reason: Sorry guys for the delay, I was in a serious accident and out of commission for the past few months, I'm just slowly recovering now, please bare with me as i try to attend to this project, it may take me awhile as I have other projects that are on standby, I'm not 100% at the moment, so im extending the deadline for 2 weeks right now. Thanks for your patience.
Hospitality

```html
<!DOCTYPE html>
<html lang="en">
<head>
<meta charset="utf-8">
<title>Corin Vale Hospitality College – Business Card</title>
<link rel="stylesheet" href="https://fonts.googleapis.com/css2?family=Pinyon+Script&family=PT+Sans:wght@400;700&display=swap">
<style>
  :root {
    --canvas: #ffffff;
    --gold-dark: #8f5f1a;
    --gold-mid: #c4952f;
    --gold-light: #f7edb0;
    --gold-bright: #fffbe6;
    --gold-field: #d9ab4a;
    --gold-field-light: #eccb6c;
    --edge-line: #5a2a0c;
    --ink: #3a2f00;
    --ink-soft: #4a3506;
    --logo-white: #ffffff;
    --metal: linear-gradient(90deg, #94601c 0%, #c18b2c 10%, #f8eeb4 22%, #b8841f 34%, #f3e39a 46%, #fffdf0 56%, #e0c06a 66%, #f8ebac 74%, #a8741e 86%, #9a6420 100%);
  }
  * { margin: 0; padding: 0; box-sizing: border-box; }
  html, body {
    width: 1200px; height: 1000px; overflow: hidden;
    background: var(--canvas);
  }
  .sheet { position: relative; width: 1200px; height: 1000px; }

  .card { position: absolute; overflow: hidden; background: var(--gold-field); }
  .card--front { left: 14px; top: 33px; width: 742px; height: 462px; background: transparent; }
  .card--back  { left: 436px; top: 518px; width: 742px; height: 447px; }

  .metal-band { position: absolute; left: 0; width: 100%; background: var(--metal); }
  .edge-line { position: absolute; left: 0; width: 100%; height: 2px; background: var(--edge-line); }
  .hairline { position: absolute; left: 0; width: 100%; height: 4px; background: var(--metal); }

  .pattern-field {
    position: absolute; left: 0; width: 100%;
    background:
      repeating-linear-gradient(0deg, rgba(255,255,255,0.06) 0 2px, rgba(0,0,0,0.03) 2px 4px),
      radial-gradient(ellipse at 30% 40%, var(--gold-field-light), var(--gold-field) 55%, #c08f36 100%);
  }
  .brushed-panel {
    position: absolute; left: 0; width: 100%;
    background:
      repeating-linear-gradient(0deg, rgba(255,255,255,0.10) 0 2px, rgba(150,100,20,0.08) 2px 5px),
      linear-gradient(90deg, #e2b950, #f3d77c 35%, #f7e08e 55%, #e8c25e 80%, #dcb24a);
  }

  .script-title {
    position: absolute; left: 176px; top: 128px;
    font-family: "Pinyon Script", cursive;
    color: var(--ink-soft);
    font-size: 54px; line-height: 46px;
  }
  .script-title .indent { display: block; }
  .script-title .l2 { padding-left: 12px; }
  .script-title .l3 { padding-left: 4px; }
  .script-title .gap { padding-left: 26px; }

  .brand {
    position: absolute; left: 20px; top: 62px;
    display: flex; align-items: center; gap: 16px;
    font-family: "PT Sans", sans-serif; font-weight: 700;
    color: var(--logo-white);
  }
  .brand-square { width: 86px; height: 118px; background: var(--logo-white); }
  .brand-name { font-size: 40px; line-height: 38px; text-transform: uppercase; letter-spacing: 0.5px; }
  .brand-name small { display: block; font-size: 15px; line-height: 20px; letter-spacing: 1px; }

  .contact {
    position: absolute; right: 18px; top: 196px;
    text-align: right; font-family: "PT Sans", sans-serif; color: var(--ink);
  }
  .contact-name { font-size: 42px; font-weight: 700; line-height: 44px; letter-spacing: 0.5px; }
  .contact-role { font-size: 27px; line-height: 32px; color: var(--ink-soft); margin-right: 4px; }
  .contact-lines { margin-top: 14px; font-size: 18px; line-height: 23px; }
  .contact-lines .spacer { height: 20px; }
</style>
</head>
<body>
<main class="sheet">

  <section class="card card--front" aria-label="Card front">
    <div class="hairline" style="top:0"></div>
    <div class="metal-band" style="top:10px;height:37px"></div>
    <div class="edge-line" style="top:47px"></div>
    <div class="pattern-field" role="img" aria-label="Gold paisley swirl pattern" style="top:49px;height:373px"></div>
    <div class="edge-line" style="top:422px"></div>
    <div class="metal-band" style="top:425px;height:37px"></div>
    <h1 class="script-title">
      <span class="indent l1">Corin</span>
      <span class="indent l2">Vale</span>
      <span class="indent l3">Hospitality<span class="gap"></span>College</span>
    </h1>
  </section>

  <section class="card card--back" aria-label="Card back">
    <div class="metal-band" style="top:0;height:35px"></div>
    <div class="edge-line" style="top:35px"></div>
    <div class="pattern-field" role="img" aria-label="Gold paisley swirl pattern" style="top:37px;height:205px"></div>
    <div class="brushed-panel" style="top:242px;height:168px"></div>
    <div class="edge-line" style="top:410px"></div>
    <div class="metal-band" style="top:412px;height:35px"></div>

    <div class="brand">
      <span class="brand-square"></span>
      <span class="brand-name">Corin Vale<small>Hospitality College</small></span>
    </div>

    <div class="contact">
      <p class="contact-name">TOBIN MARSH</p>
      <p class="contact-role">Director</p>
      <div class="contact-lines">
        <p>Phone: 1300 615 737</p>
        <p>Mobile: 0455 817 296</p>
        <div class="spacer"></div>
        <p>Email: info@corinvale.example</p>
        <p>website: www.corinvale.example</p>
      </div>
    </div>
  </section>

</main>
</body>
</html>
```